female esthetician looking for an impact business card

I an an expert in skin care industry with high experience in NYC.I want my business card to look professional , an impact at first look. I do want a combination between white and gold . I believe the font will be great if is gold.. The Fonts are also important. MARISELA VONDRAKE (SKIN CARE BOUTIQUE)

THIS SHOULD BE THE BUSINESS NAME, and should be placed on th eback of the card.
IN front m, the name MARISELA VONDRAKE - ESTHETCIAN

BY APPOINTMENTS ONLY: 555.218.9031

Target Market(s)

HIGH END CLIENTELE

Contact Information for Business Card

iT WILL BE on a luxury paper. I neeed the wow feeling

Requirements
Should not have
• pictures

```html
<!DOCTYPE html>
<html lang="en">
<head>
<meta charset="utf-8">
<title>Marisela Vondrake — Skin Care Expert Business Card</title>
<link href="https://fonts.googleapis.com/css2?family=Cinzel:wght@500;600&family=Comfortaa:wght@400&family=Montserrat:wght@400&display=swap" rel="stylesheet">
<style>
  :root{
    --backdrop:#d9d9d9;
    --card:#fbfaf2;
    --gold-deep:#b8862a;
    --gold:#d4a640;
    --gold-light:#f3dc96;
    --ink-grey:#8a8a8a;
    --photo-light:#f1ebe6;
    --photo-mid:#e3cfc3;
    --photo-dark:#b89a88;
  }
  *{margin:0;padding:0;box-sizing:border-box}
  html,body{width:1200px;height:1000px;overflow:hidden;background:var(--backdrop)}
  .canvas{position:relative;width:1200px;height:1000px}
  .business-card{
    position:absolute;left:100px;top:214px;width:1000px;height:572px;
    background:var(--card);overflow:hidden;
    box-shadow:0 10px 30px rgba(0,0,0,.12);
  }
  .card-art{position:absolute;inset:0;width:100%;height:100%}
  .identity{position:absolute;left:425px;top:130px;width:480px;text-align:center}
  .identity-name{
    font-family:"Cinzel",serif;font-weight:600;font-size:40px;letter-spacing:.5px;
    color:var(--gold-deep);line-height:1;white-space:nowrap;
  }
  .identity-role{
    font-family:"Comfortaa",sans-serif;font-size:30px;letter-spacing:2px;
    color:var(--gold);margin-top:12px;line-height:1;
  }
  .contact-list{
    position:absolute;left:470px;top:320px;list-style:none;
    font-family:"Montserrat",sans-serif;font-size:22px;color:var(--ink-grey);line-height:1.45;
  }
  .contact-item{display:flex;align-items:flex-start;gap:12px}
  .contact-icon{width:20px;height:20px;flex:none;margin-top:5px}
  .contact-item.address{flex-direction:column;gap:0}
  .address-line{display:flex;gap:12px}
  .address-line .spacer{width:20px;flex:none}
</style>
</head>
<body>
<main class="canvas">
  <article class="business-card">
    <svg class="card-art" viewBox="0 0 1000 572" preserveAspectRatio="none">
      <defs>
        <linearGradient id="photoTone" x1="0" y1="0" x2="1" y2="1">
          <stop offset="0" stop-color="var(--photo-light)"/>
          <stop offset=".55" stop-color="var(--photo-mid)"/>
          <stop offset="1" stop-color="var(--photo-dark)"/>
        </linearGradient>
        <linearGradient id="goldBand" x1="0" y1="0" x2="1" y2="0">
          <stop offset="0" stop-color="var(--gold-deep)"/>
          <stop offset=".45" stop-color="var(--gold-light)"/>
          <stop offset="1" stop-color="var(--gold)"/>
        </linearGradient>
      </defs>
      <path class="gold-swoosh-outer" d="M330 0 H372 C300 180 310 400 430 572 H380 C270 400 262 180 330 0 Z" fill="url(#goldBand)"/>
      <path class="gold-swoosh-inner" d="M318 0 H345 C275 180 280 400 400 572 H370 C258 400 250 180 318 0 Z" fill="var(--gold-deep)" opacity=".85"/>
      <path class="treatment-photo" role="img" aria-label="Photo of a client relaxing during a facial treatment" d="M0 0 H322 C254 180 262 400 372 572 H0 Z" fill="url(#photoTone)"/>
      <path class="gold-edge-swoosh" d="M1000 150 C960 260 930 420 850 572 H872 C950 430 985 300 1000 210 Z" fill="url(#goldBand)"/>
    </svg>

    <header class="identity">
      <h1 class="identity-name">MARISELA VONDRAKE</h1>
      <p class="identity-role">skin care expert</p>
    </header>

    <ul class="contact-list">
      <li class="contact-item phone">
        <svg class="contact-icon" viewBox="0 0 24 24"><path d="M6.6 2.5l3 3.6-1.9 2.3c1.2 2.7 3.2 4.7 5.9 5.9l2.3-1.9 3.6 3-1.8 3.6C10.7 19 5 13.3 3 6.3z" fill="var(--gold)"/></svg>
        <span>+1.800.555.0142</span>
      </li>
      <li class="contact-item email">
        <svg class="contact-icon" viewBox="0 0 24 24"><rect x="2.5" y="5" width="19" height="14" fill="none" stroke="var(--gold)" stroke-width="2"/><path d="M3 6l9 7 9-7M3 18l7-6M21 18l-7-6" fill="none" stroke="var(--gold)" stroke-width="1.6"/></svg>
        <span>info@mariselavondrake.com</span>
      </li>
      <li class="contact-item address">
        <span class="address-line">
          <svg class="contact-icon" viewBox="0 0 24 24"><path d="M12 2a7 7 0 0 0-7 7c0 5 7 13 7 13s7-8 7-13a7 7 0 0 0-7-7z" fill="var(--gold)"/><circle cx="12" cy="9" r="2.6" fill="var(--card)"/></svg>
          <span>Level 3, 18 Linden Lane</span>
        </span>
        <span class="address-line"><span class="spacer"></span><span>Fairhaven, Australia</span></span>
      </li>
    </ul>
  </article>
</main>
</body>
</html>
```